Lantern Method of Ascent Programme Graphic

Please refer to attached graphic.
I wish to redesign this graphic to represent a programme of work that we (Vendro) deliver to our customers.
The design represents 9 steps ( 3 steps at each of 3 levels) and is all about implementing the 'Lantern Method of Ascent'

I like the fact that the increasing business growth is evident when you are progressing through the stages, but the current graphic looks dated and the colours are not working.
I would also like to incorporate the LMA logo we have created.

Target Market(s)

IT Sector - businesses looking to grow

Industry/Entity Type

We are a digital marketing company

Requirements
Must have
• Clear, concise design
Should not have
• Design must not be complicated

```html
<!DOCTYPE html>
<html lang="en">
<head>
<meta charset="utf-8">
<title>Lantern Method of Ascent – Programme</title>
<link rel="stylesheet" href="https://fonts.googleapis.com/css2?family=Lexend+Exa:wght@600;700;800&display=swap">
<style>
  :root {
    --bg-deep: #1b3a8a;
    --bg-mid: #23509e;
    --white: #ffffff;
    --navy-text: #1c2a8c;
    --pill-blue-a: #2a6bff;
    --pill-blue-b: #1437c8;
    --purple-a: #a88ad6;
    --purple-b: #7a1e93;
    --purple-foot-a: #d99cdc;
    --purple-foot-b: #a77ad9;
    --blue-a: #22b4f4;
    --blue-b: #011a86;
    --blue-foot-a: #1aa6ee;
    --blue-foot-b: #3be4ff;
    --green-a: #26d63a;
    --green-b: #04613d;
    --green-foot-a: #0fb45a;
    --green-foot-b: #74ec92;
    --brand: #3d63f0;
  }
  * { margin: 0; padding: 0; box-sizing: border-box; }
  html, body { width: 1200px; height: 755px; overflow: hidden; }
  body { font-family: "Lexend Exa", "Arial Black", sans-serif; color: var(--white); }
  .canvas { position: relative; width: 1200px; height: 755px; overflow: hidden;
    background: linear-gradient(160deg, #1a2e8c 0%, #1f4aa4 45%, #2a5aa8 100%); }
  .backdrop { position: absolute; inset: 0; }
  .abs { position: absolute; }

  .value-frame { left: 28px; top: 58px; width: 359px; height: 81px; border-radius: 41px;
    border: 1px solid rgba(140,170,255,.55); }
  .value-pill { left: 36px; top: 69px; width: 343px; height: 58px; border-radius: 29px;
    background: linear-gradient(90deg, var(--pill-blue-a), var(--pill-blue-b));
    box-shadow: 0 0 14px rgba(60,110,255,.6);
    display: flex; align-items: center; justify-content: center;
    font-size: 26px; font-weight: 700; letter-spacing: 1px; text-shadow: 0 0 8px rgba(255,255,255,.7); }

  .stage-label { display: flex; align-items: center; justify-content: center;
    border-radius: 28px; font-size: 23px; font-weight: 700; letter-spacing: 1px; }
  .label-rhythmic { left: 312px; top: 365px; width: 178px; height: 55px;
    background: linear-gradient(110deg, #b89ad8 0%, #a85aa8 55%, #951a98 100%); }
  .label-acquisition { left: 562px; top: 287px; width: 229px; height: 60px;
    background: linear-gradient(110deg, #3ac0f6 0%, #2ee6ff 40%, #1e62ff 100%); }
  .label-customers { left: 864px; top: 215px; width: 209px; height: 55px;
    background: linear-gradient(110deg, #23c8d8 0%, #1ff0ee 35%, #0fd070 70%, #18c040 100%); }

  .step-number { width: 82px; height: 82px; border-radius: 50%; display: flex;
    align-items: center; justify-content: center; font-family: "Lexend Exa", sans-serif;
    font-size: 52px; font-weight: 600; }
  .step-1 { left: 356px; top: 268px; background: linear-gradient(135deg, #c4d2ea 45%, #8a5a98 55%, #8a2a80 100%); border: 1px solid #d43aa0; }
  .step-2 { left: 635px; top: 190px; background: linear-gradient(135deg, #3ad4f8 45%, #7ad8ff 55%, #1a5aff 100%); }
  .step-3 { left: 927px; top: 113px; background: linear-gradient(135deg, #16b830 45%, #3ef0ea 55%, #0fa040 100%); }

  .column { overflow: hidden; border-radius: 52px 52px 0 0; }
  .col-foundation { left: 250px; top: 442px; width: 287px; height: 234px;
    background: linear-gradient(100deg, var(--purple-a), var(--purple-b)); border: 1px solid rgba(190,150,230,.6); }
  .col-tactical { left: 540px; top: 360px; width: 273px; height: 316px;
    background: linear-gradient(120deg, var(--blue-a) 0%, #0a6ae0 50%, var(--blue-b) 100%); border: 1px solid #1aa0ff; }
  .col-strategic { left: 816px; top: 281px; width: 274px; height: 395px;
    background: linear-gradient(120deg, var(--green-a) 0%, #0a8a3a 50%, var(--green-b) 100%); border: 1px solid #2ce840; }

  .item-list { list-style: none; }
  .item { position: relative; display: flex; align-items: center;
    font-size: 21px; font-weight: 700; letter-spacing: 1px; }
  .item::before { content: ""; position: absolute; width: 11px; height: 11px; border-radius: 50%; background: var(--white); }
  .col-foundation .item { height: 51px; padding-left: 63px; border-bottom: 2px solid rgba(200,160,235,.7); }
  .col-foundation .item:first-child { height: 54px; }
  .col-foundation .item::before { left: 27px; }
  .col-tactical .item { height: 58px; padding-left: 56px; border-bottom: 2px solid #1ab0ff; }
  .col-tactical .item:last-child { border-bottom: none; }
  .col-tactical .item::before { left: 28px; }
  .col-strategic .item { height: 53px; padding-left: 56px; border-bottom: 2px solid #21d232; }
  .col-strategic .item:last-child { border-bottom: none; }
  .col-strategic .item::before { left: 29px; }

  .scorecard { position: absolute; left: 0; right: 0; bottom: 0; height: 82px;
    display: flex; flex-direction: column; align-items: center; justify-content: center; gap: 6px; }
  .col-foundation .scorecard { background: linear-gradient(160deg, var(--purple-foot-a), var(--purple-foot-b)); }
  .col-tactical .scorecard { background: linear-gradient(90deg, var(--blue-foot-a), var(--blue-foot-b)); }
  .col-strategic .scorecard { background: linear-gradient(90deg, var(--green-foot-a), var(--green-foot-b)); }
  .scorecard-title { font-size: 14.5px; font-weight: 800; letter-spacing: .5px; }
  .scorecard-sub { font-size: 13.5px; font-weight: 800; color: var(--navy-text); letter-spacing: .5px; }

  .brand-name { left: 950px; top: 703px; font-size: 30px; font-weight: 700; color: var(--brand); letter-spacing: 1px; }
  .method-name { left: 1118px; top: 706px; font-size: 24px; font-weight: 700; color: #8a9ae8; }
</style>
</head>
<body>
<main class="canvas">
  <svg class="backdrop" width="1200" height="755" viewBox="0 0 1200 755" aria-hidden="true">
    <defs>
      <linearGradient id="ascent-band" x1="0" y1="1" x2="1" y2="0">
        <stop offset="0" stop-color="#3a7ad0" stop-opacity=".15"/>
        <stop offset="1" stop-color="#4a9ae0" stop-opacity=".85"/>
      </linearGradient>
      <linearGradient id="floor-strip" x1="0" y1="0" x2="0" y2="1">
        <stop offset="0" stop-color="#9ab4e0" stop-opacity=".75"/>
        <stop offset="1" stop-color="#5a80d0" stop-opacity=".5"/>
      </linearGradient>
      <linearGradient id="base-band" x1="0" y1="0" x2="1" y2="0">
        <stop offset="0" stop-color="#4ab0e8"/>
        <stop offset=".3" stop-color="#0d8ed8"/>
        <stop offset=".75" stop-color="#2a5ab8"/>
        <stop offset="1" stop-color="#4a2a90"/>
      </linearGradient>
      <linearGradient id="base-glow" x1="0" y1="0" x2="1" y2="0">
        <stop offset="0" stop-color="#ffffff" stop-opacity=".1"/>
        <stop offset="1" stop-color="#ffffff" stop-opacity=".95"/>
      </linearGradient>
    </defs>
    <polygon points="0,378 1200,0 0,0" fill="url(#ascent-band)" opacity=".7"/>
    <polygon points="0,0 1200,0 0,378" fill="#1a2e8c" opacity=".35"/>
    <rect x="0" y="592" width="1200" height="84" fill="url(#floor-strip)"/>
    <rect x="0" y="676" width="1200" height="79" fill="url(#base-band)"/>
    <polygon points="0,676 412,676 325,755 0,755" fill="url(#base-glow)" opacity=".7"/>
    <polyline points="182,42 201,7 220,42" fill="none" stroke="#3a5ac8" stroke-width="6"/>
    <line x1="201" y1="155" x2="201" y2="676" stroke="#dfe8ff" stroke-width="5" stroke-linecap="round" opacity=".9"/>
    <g stroke="#ffffff" stroke-width="1.6" fill="none">
      <polyline points="434,301 528,301 615,243"/>
      <polyline points="738,222 826,220 914,166"/>
      <line x1="996" y1="110" x2="1075" y2="52"/>
      <polyline points="1062,52 1075,52 1075,63"/>
    </g>
    <circle cx="528" cy="301" r="5.5" fill="#fff"/>
    <circle cx="826" cy="220" r="5.5" fill="#fff"/>
  </svg>

  <div class="abs value-frame"></div>
  <div class="abs value-pill">BUSINESS VALUE</div>

  <div class="abs step-number step-1">1</div>
  <div class="abs step-number step-2">2</div>
  <div class="abs step-number step-3">3</div>

  <div class="abs stage-label label-rhythmic">RHYTHMIC</div>
  <div class="abs stage-label label-acquisition">ACQUISITION</div>
  <div class="abs stage-label label-customers">CUSTOMERS</div>

  <section class="abs column col-foundation">
    <ul class="item-list">
      <li class="item">PERSONAS</li>
      <li class="item">DATABASE</li>
      <li class="item">SYSTEMS</li>
    </ul>
    <div class="scorecard">
      <span class="scorecard-title">NUMBERS THAT MATTER</span>
      <span class="scorecard-sub">FOUNDATION METRICS</span>
    </div>
  </section>

  <section class="abs column col-tactical">
    <ul class="item-list">
      <li class="item">MESSAGING</li>
      <li class="item">LEADS</li>
      <li class="item">PIPELINE</li>
    </ul>
    <div class="scorecard">
      <span class="scorecard-title">WEEKLY SCOREDCARD</span>
      <span class="scorecard-sub">TACTICAL EXECUTION</span>
    </div>
  </section>

  <section class="abs column col-strategic">
    <ul class="item-list">
      <li class="item">SALES</li>
      <li class="item">NURTURE</li>
      <li class="item">REFERENCE</li>
    </ul>
    <div class="scorecard">
      <span class="scorecard-title">MONTHLY SCORECARD</span>
      <span class="scorecard-sub">STRATEGIC REVIEW</span>
    </div>
  </section>

  <div class="abs brand-name">VENDRO</div>
  <div class="abs method-name">LMA</div>
</main>
</body>
</html>
```